Bespoke Builders Business Card Design

We need a business card for an established builder of high quality bespoke homes in Auckland and Northland. We build and renovate homes collaboratively facilitating effective communication between owners, builders, architects, suppliers and tradespeople. We have never built or renovated a home that leaks or has faults. We only use reliable materials. We have never been sued or had legal action taken against us. We are honest builders of bespoke homes not group mass produced homes. Our niche market is in character homes. We practice sustainability and have built a lot of coastal property. We have been in business for over thirty years . We would like to see natural colors of the environment sand,sea and maybe vegetation . The design should communicate quality, sustainability,fair pricing, open communication and the originality of bespoke building. And the fact that the builder is registered.

Business

Dale Morvick Builders
Ph. 021583917
58 Harlow Rd Kerrigan Bay Auckland 0915
PO Box 287 Tawharu 0563

```html
<!DOCTYPE html>
<html lang="en">
<head>
<meta charset="utf-8">
<title>Dale Morvick Builders – Business Card</title>
<link rel="stylesheet" href="https://fonts.googleapis.com/css2?family=Questrial&display=swap">
<style>
  :root {
    --backdrop: #151a24;
    --card-dark: #1b1c1e;
    --card-light: #ffffff;
    --sand: #e09a2c;
    --sea: #7ecfdc;
    --ink: #8a8f96;
    --icon: #5fc3d3;
  }
  * { margin: 0; padding: 0; box-sizing: border-box; }
  html, body { width: 1200px; height: 900px; overflow: hidden; }
  body {
    background: var(--backdrop);
    font-family: "Questrial", "Century Gothic", sans-serif;
    position: relative;
  }
  .card {
    position: absolute;
    left: 285px;
    width: 630px;
    height: 360px;
    border-radius: 22px;
    overflow: hidden;
  }
  .card--front {
    top: 70px;
    background: linear-gradient(160deg, #26272a, var(--card-dark) 60%, #121314);
    display: flex;
    align-items: center;
    justify-content: center;
  }
  .card--back {
    top: 470px;
    background: var(--card-light);
  }
  .brand-name {
    color: var(--sand);
    font-size: 38px;
    letter-spacing: 1px;
    line-height: 1.1;
    text-align: center;
  }
  .card--back .brand-name {
    position: absolute;
    top: 42px;
    right: 40px;
    font-size: 26px;
    text-align: right;
  }
  .contact-list {
    position: absolute;
    left: 40px;
    top: 150px;
    list-style: none;
  }
  .contact-list li {
    display: flex;
    align-items: center;
    gap: 12px;
    color: var(--ink);
    font-size: 20px;
    letter-spacing: 0.5px;
    margin-bottom: 10px;
  }
  .contact-list svg { width: 18px; height: 18px; flex: none; }
  .wave { position: absolute; left: 0; bottom: 0; width: 630px; height: 360px; }
</style>
</head>
<body>
  <section class="card card--front">
    <p class="brand-name">Dale Morvick Builders</p>
  </section>

  <section class="card card--back">
    <p class="brand-name">Dale Morvick Builders</p>

    <svg class="wave" viewBox="0 0 630 360" aria-hidden="true">
      <path d="M300 235 C 430 215, 560 165, 630 120 L630 175 C 560 205, 430 230, 300 235 Z" fill="var(--sea)"/>
      <path d="M0 300 C 150 250, 330 235, 450 228 C 540 222, 600 200, 630 182 L630 360 L0 360 Z" fill="var(--sand)"/>
    </svg>

    <ul class="contact-list">
      <li>
        <svg viewBox="0 0 20 20"><path fill="var(--icon)" d="M2 7c0-2 3-4 8-4s8 2 8 4v1.5h-4V7H6v1.5H2Zm3 3h10l2 7H3Zm5 1.5a2.5 2.5 0 1 0 0 5a2.5 2.5 0 1 0 0-5Z"/></svg>
        021583917
      </li>
      <li>
        <svg viewBox="0 0 20 20"><path fill="var(--icon)" d="M10 1a6 6 0 0 0-6 6c0 4.5 6 12 6 12s6-7.5 6-12a6 6 0 0 0-6-6Zm0 8.5a2.5 2.5 0 1 1 0-5a2.5 2.5 0 0 1 0 5Z"/></svg>
        58 Harlow Rd Kerrigan Bay Auckland 0915
      </li>
      <li>
        <svg viewBox="0 0 20 20"><path fill="var(--icon)" d="M10 1a6 6 0 0 0-6 6c0 4.5 6 12 6 12s6-7.5 6-12a6 6 0 0 0-6-6Zm0 8.5a2.5 2.5 0 1 1 0-5a2.5 2.5 0 0 1 0 5Z"/></svg>
        PO Box 287 Tawharu 0563
      </li>
    </ul>
  </section>
</body>
</html>
```